Business cards Design for advertising technology Argentur

Hi guys,

we need a cool, simple business card design for our Company "Zentravio17".
It should be clean, but also special - it should be an eye catcher!

Our Logo is attached.
The format should be 85x55m.

The adress is:
Obere Kranzinger Str. 14.
9512 Tallbrunn
Tel: 04251 62914

```html
<!DOCTYPE html>
<html lang="de">
<head>
<meta charset="utf-8">
<title>Zentravio17 – Visitenkarte</title>
<link rel="stylesheet" href="https://fonts.googleapis.com/css2?family=Lato:wght@400;700;900&display=swap">
<style>
  :root {
    --page: #1c1c1e;
    --card: #262627;
    --accent: #f39a1e;
    --ink: #ffffff;
    --muted: #e4e4e4;
    --faint: #3d3d3f;
  }
  * { box-sizing: border-box; margin: 0; padding: 0; }
  html, body { width: 1200px; height: 948px; overflow: hidden; }
  body {
    background: var(--page);
    font-family: "Lato", sans-serif;
    display: flex;
    align-items: center;
    justify-content: center;
    gap: 40px;
  }
  .card {
    position: relative;
    width: 540px;
    height: 349px;
    background: var(--card);
    border-bottom: 4px solid var(--accent);
    border-left: 4px solid var(--accent);
    overflow: hidden;
  }
  /* back side */
  .card--back {
    display: flex;
    align-items: center;
    justify-content: center;
    gap: 14px;
    padding-bottom: 40px;
  }
  .card--back .brand-mark {
    width: 46px; height: 46px;
    background: var(--faint);
  }
  .card--back .brand-name {
    color: var(--faint);
    font-weight: 900;
    font-size: 38px;
    letter-spacing: 0.02em;
    text-transform: uppercase;
  }
  /* front side */
  .card--front { display: flex; }
  .brand {
    width: 250px;
    display: flex;
    flex-direction: column;
    align-items: center;
    justify-content: flex-end;
    gap: 16px;
    padding-bottom: 86px;
  }
  .brand .brand-mark {
    width: 74px; height: 74px;
    border-radius: 50%;
    background: var(--ink);
  }
  .brand .brand-name {
    color: var(--ink);
    font-weight: 900;
    font-size: 26px;
    text-transform: uppercase;
    letter-spacing: 0.01em;
    white-space: nowrap;
  }
  .divider {
    width: 2px;
    background: var(--accent);
    margin: 62px 0 80px;
  }
  .contact {
    padding: 60px 0 0 22px;
    color: var(--muted);
    font-size: 15px;
    line-height: 1.45;
  }
  .contact .person {
    color: var(--accent);
    font-weight: 700;
    font-size: 20px;
    text-transform: uppercase;
    letter-spacing: 0.02em;
  }
  .contact .role { margin-bottom: 12px; }
  .contact .address { margin-bottom: 8px; }
  .contact ul { list-style: none; }
  .contact li { display: flex; align-items: center; gap: 10px; margin-bottom: 4px; white-space: nowrap; }
  .contact svg { width: 16px; height: 16px; flex: none; }
</style>
</head>
<body>
  <section class="card card--back" aria-label="Kartenrückseite">
    <span class="brand-mark"></span>
    <span class="brand-name">Zentravio17</span>
  </section>

  <section class="card card--front" aria-label="Kartenvorderseite">
    <div class="brand">
      <span class="brand-mark"></span>
      <span class="brand-name">Zentravio17</span>
    </div>
    <div class="divider"></div>
    <div class="contact">
      <p class="person">Lena Hartmann</p>
      <p class="role">Director</p>
      <p class="address">Obere Kranzinger Str. 14.<br>9512 Tallbrunn</p>
      <ul>
        <li>
          <svg viewBox="0 0 16 16" aria-hidden="true"><circle cx="8" cy="8" r="8" fill="#f39a1e"/><path d="M5.2 4.2l1.4-.2.8 1.8-.9.7c.5 1 1.2 1.8 2.2 2.3l.7-.9 1.8.8-.2 1.4c-3.2.2-5.9-2.6-5.8-5.9z" fill="#262627"/></svg>
          04251 62914
        </li>
        <li>
          <svg viewBox="0 0 16 16" aria-hidden="true"><circle cx="8" cy="8" r="8" fill="#f39a1e"/><rect x="4" y="5" width="8" height="6" rx="1" fill="#262627"/><path d="M4.3 5.4L8 8.3l3.7-2.9" stroke="#f39a1e" stroke-width="1" fill="none"/></svg>
          info@zentravio17.example
        </li>
        <li>
          <svg viewBox="0 0 16 16" aria-hidden="true"><circle cx="8" cy="8" r="8" fill="#f39a1e"/><circle cx="8" cy="8" r="4" fill="none" stroke="#262627" stroke-width="1.2"/><path d="M4 8h8M8 4c-1.6 2.4-1.6 5.6 0 8M8 4c1.6 2.4 1.6 5.6 0 8" stroke="#262627" stroke-width="1" fill="none"/></svg>
          www.zentravio17.example
        </li>
      </ul>
    </div>
  </section>
</body>
</html>
```